Dental Business Card Design w/logo

Classic, elegant w/a touch of contemporary
Upscale dental facility located in Modesto CA
Specializing in restorative & general dentistry
Providing exceptional customer service to the community
Updates

I prefer script and not bold writing
If you can use the phone; fax and email icons instead of spelling them out, it would be great
No bold colors
Classy and elegant
In the back of the card I would like to see something like this
Your Next Appointment:
Mon     Tue    Wed    Thur (a box next to each of them for marking)
Date:_______________ at_____________ AM    PM  (a box next to them for marking)

Thank you

Target Market(s)

Well established professional

Industry/Entity Type

Dental

Contact Information for Business Card

Lavinteya Morbundi DMD
4176 Larkspur Rd
Suite F7
Pellorin, CA 90412

Office: 555-731-5902
Fax: 555-731-8417
Email: morbundidmd@velmoranet.com

Requirements
Must have
• Unique classic logo
An easily repeatable design that can be used on letterhead and envelopes
Nice to have
• My initials incorporated into unique design
Should not have
• No cartoons or cheesy themes. This is a practice for the well established and professional individual.

```html
<!DOCTYPE html>
<html lang="en">
<head>
<meta charset="utf-8">
<title>Lavinteya Morbundi DMD – Business Card</title>
<link rel="stylesheet" href="https://fonts.googleapis.com/css2?family=EB+Garamond:ital,wght@0,400;1,400&display=swap">
<style>
  :root {
    --backdrop: #e9e9e7;
    --card: #ffffff;
    --ink: #6e6e6e;
    --ink-soft: #8a8a8a;
    --teal: #7fcfcf;
    --teal-deep: #5bb8b8;
    --rule: #a9a9a9;
  }
  * { box-sizing: border-box; margin: 0; padding: 0; }
  html, body {
    width: 1200px; height: 873px; overflow: hidden;
    background: var(--backdrop);
    font-family: "EB Garamond", Georgia, serif;
    color: var(--ink);
  }
  .canvas {
    position: relative; width: 1200px; height: 873px;
    display: flex; justify-content: center; align-items: center; gap: 70px;
  }
  .card {
    position: relative; width: 300px; height: 525px;
    background: var(--card);
    box-shadow: 0 2px 10px rgba(0,0,0,0.12);
  }

  /* Back: appointment card */
  .appointment { padding: 110px 26px 0; text-align: center; }
  .appointment-title { font-size: 17px; font-weight: 400; letter-spacing: 1.5px; margin-bottom: 14px; }
  .days { display: flex; flex-wrap: wrap; justify-content: center; gap: 6px 12px; font-size: 12.5px; font-style: italic; margin-bottom: 18px; }
  .check { display: inline-flex; align-items: center; gap: 3px; }
  .box { width: 8px; height: 8px; border: 1px solid var(--ink); display: inline-block; }
  .field { display: flex; align-items: flex-end; gap: 6px; font-size: 14px; font-style: italic; margin: 0 0 14px 20px; }
  .dots { flex: 0 0 120px; border-bottom: 1px dotted var(--rule); height: 12px; }
  .field .check { font-style: normal; font-size: 12.5px; margin-left: 4px; }
  .notice {
    position: absolute; left: 24px; right: 24px; bottom: 62px;
    font-size: 13px; font-style: italic; line-height: 1.35; text-align: center; color: var(--ink-soft);
  }

  /* Front: identity card */
  .identity { text-align: center; padding-top: 40px; }
  .brand { display: flex; flex-direction: column; align-items: center; gap: 8px; }
  .brand-dot { width: 56px; height: 56px; border-radius: 50%; background: var(--teal); }
  .brand-name { font-size: 16px; font-weight: 400; letter-spacing: 2px; color: var(--teal-deep); }
  .doctor { margin-top: 34px; font-size: 13px; font-weight: 400; letter-spacing: 1.5px; text-transform: uppercase; }
  .specialty { font-size: 12px; font-style: italic; color: var(--ink-soft); margin-top: 2px; }
  .contact {
    position: absolute; right: 26px; top: 268px;
    text-align: right; font-size: 11.5px; line-height: 1.35;
  }
  .contact address { font-style: normal; margin-bottom: 10px; }
  .contact .label { color: var(--teal-deep); margin-right: 3px; }
  .contact .email { color: var(--teal-deep); margin-top: 8px; display: block; }
</style>
</head>
<body>
<main class="canvas">

  <section class="card appointment" aria-label="Appointment card">
    <h2 class="appointment-title">Your Next Appointment:</h2>
    <div class="days">
      <span class="check"><i class="box"></i>Mon.</span>
      <span class="check"><i class="box"></i>Tue.</span>
      <span class="check"><i class="box"></i>Wed.</span>
      <span class="check"><i class="box"></i>Thur.</span>
      <span class="check"><i class="box"></i>Fri.</span>
    </div>
    <div class="field">Date: <span class="dots"></span>
      <span class="check"><i class="box"></i>am</span>
      <span class="check"><i class="box"></i>pm</span>
    </div>
    <div class="field">Time: <span class="dots"></span></div>
    <p class="notice">If unable to keep this appointment, kindly give 48 hours notice, otherwise a charge will be made for time reserved.</p>
  </section>

  <section class="card identity" aria-label="Business card">
    <div class="brand">
      <span class="brand-dot"></span>
      <span class="brand-name">Morbundi Dental</span>
    </div>
    <h1 class="doctor">Lavinteya Morbundi, D.M.D.</h1>
    <p class="specialty">Restorative &amp; General Dentistry</p>
    <div class="contact">
      <address>4176 Larkspur Rd, Suite F7<br>Pellorin, CA 90412</address>
      <div><span class="label">T:</span>555 731 5902</div>
      <div><span class="label">F:</span>555 731 8417</div>
      <span class="email">morbundidmd@velmoranet.com</span>
    </div>
  </section>

</main>
</body>
</html>
```